Tree Service Billboard 20x8 ft

We need a billboard design for a tree service company.
The billboard is 20ft x 8 ft so we need a design that is capable to stretching to those dimensions without loosing quality.
I have attached a series of images.
Image 1- Simply a billboard that I think looks good that I would like you to use for inspiration. I am aiming for the same format only no color in the wording, just black white, or gray. I like the the trees in the background, the logo placed to the left, and wording on the right.
Image 2- Current Logo I would like to the left of the billboard
Image 3- Another format of current logo if needed.
Image 4- A drawn out design template
Image 5- Another drawn out design template

Specific things I am looking for
-The contact number to be the largest thing on the design
-The logo on the design
-Key points to the design to say:
Tree Removal
Tree Trimming
Land Development
Stump Grinding
Storm Response
Insured
Free Bids
-The facebook logo
-The Google Logo

```html
<!DOCTYPE html>
<html lang="en">
<head>
<meta charset="utf-8">
<title>Elm's Tree Service Billboard</title>
<link rel="stylesheet" href="https://fonts.googleapis.com/css2?family=Barlow+Condensed:wght@600;700&display=swap">
<style>
  :root {
    --page: #ffffff;
    --forest-dark: #2f5a3a;
    --forest-mid: #4f7a55;
    --mist: #b9c3c9;
    --sky: #8f9eab;
    --ink: #111111;
    --slate: #666666;
    --paper: #ffffff;
  }
  * { margin: 0; padding: 0; box-sizing: border-box; }
  html, body {
    width: 1200px; height: 706px; overflow: hidden;
    background: var(--page);
    font-family: "Barlow Condensed", "Arial Narrow", sans-serif;
  }
  .billboard {
    position: absolute; left: 160px; top: 179px;
    width: 889px; height: 354px; overflow: hidden;
  }
  .scenery {
    position: absolute; inset: 0;
    background:
      radial-gradient(ellipse 45% 55% at 62% 28%, rgba(214,220,224,.9), rgba(214,220,224,0) 70%),
      linear-gradient(180deg, var(--sky) 0%, var(--mist) 22%, var(--forest-mid) 55%, var(--forest-dark) 100%);
  }
  .scenery::before {
    content: ""; position: absolute; left: 0; top: 0; bottom: 0; width: 40%;
    background: linear-gradient(90deg, rgba(35,70,45,.85), rgba(35,70,45,0));
  }
  .brand-mark {
    position: absolute; left: 161px; top: 26px;
    width: 196px; height: 196px; border-radius: 50%;
    border: 6px solid var(--ink);
    background: rgba(255,255,255,.92);
  }
  .brand-name {
    position: absolute; left: 40px; top: 226px; width: 454px;
    text-align: center; color: var(--slate);
    font-weight: 700; font-size: 60px; line-height: 1; letter-spacing: 0.5px;
    text-transform: uppercase; white-space: nowrap;
  }
  .phone-row {
    position: absolute; left: 55px; top: 292px; width: 424px;
    display: flex; align-items: center; gap: 10px;
  }
  .phone-rule { flex: 1; height: 6px; background: var(--ink); border: 1px solid var(--paper); }
  .phone {
    color: var(--ink); font-weight: 700; font-size: 44px; line-height: 1;
    letter-spacing: 1px; white-space: nowrap;
  }
  .services {
    position: absolute; left: 512px; top: 27px; width: 377px;
    list-style: none;
  }
  .service {
    height: 42px; margin-bottom: 9.5px;
    display: flex; align-items: center; justify-content: center;
    padding-left: 28px; white-space: nowrap;
    font-weight: 700; font-size: 33px; letter-spacing: .5px;
    clip-path: polygon(30px 0, 100% 0, 100% 100%, 30px 100%, 0 50%);
  }
  .service--light { background: var(--paper); color: var(--ink); }
  .service--dark { background: var(--slate); color: var(--paper); }
</style>
</head>
<body>
  <main class="billboard">
    <div class="scenery" role="img" aria-label="Misty evergreen forest on rolling mountain slopes"></div>
    <div class="brand-mark"></div>
    <h1 class="brand-name">Elm's Tree Service</h1>
    <div class="phone-row">
      <span class="phone-rule"></span>
      <span class="phone">417-555-0148</span>
      <span class="phone-rule"></span>
    </div>
    <ul class="services">
      <li class="service service--light">TREE REMOVAL</li>
      <li class="service service--dark">TREE TRIMMING</li>
      <li class="service service--light">LAND DEVELOPMENT</li>
      <li class="service service--dark">STUMP GRINDING</li>
      <li class="service service--light">INSURED FREE BIDS</li>
      <li class="service service--dark">STORM RESPONSE</li>
    </ul>
  </main>
</body>
</html>
```